Dental Practice based in Melbourne needs header designed for mobile website

Evergrove Dental Carlton needs logo modified (better color scheme)and the header needs good use of colors (Green should be one of them) . The overall scheme is attached below. Please maintain the overall position of the logo in the center just like the way it is. Icons that should be present : Evergrove Dental Carlton, Phone number with phone icon, Menu bar, Book now, search icon, Logo. in the center.

```html
<!DOCTYPE html>
<html lang="en">
<head>
<meta charset="utf-8">
<title>Evergrove Dental Carlton – Mobile Header</title>
<link href="https://fonts.googleapis.com/css2?family=Arimo:wght@400;700&display=swap" rel="stylesheet">
<style>
  :root {
    --plum-deep: #2a0528;
    --plum: #5a1257;
    --plum-glow: #7b2f78;
    --lime: #8cc63f;
    --lime-dark: #3f9a20;
    --lavender: #a77ac6;
    --white: #ffffff;
    --violet-badge: #3b2a8c;
  }
  * { box-sizing: border-box; margin: 0; padding: 0; }
  html, body { width: 800px; height: 1200px; overflow: hidden; background: var(--white); }
  body { font-family: "Arimo", Arial, sans-serif; position: relative; }

  .site-header {
    position: absolute; left: 0; top: 0; width: 800px; height: 370px;
    background: radial-gradient(ellipse at 50% 25%, var(--plum-glow) 0%, var(--plum) 45%, var(--plum-deep) 100%);
  }
  .brand-mark { position: absolute; left: 312px; top: 24px; width: 176px; height: 176px;
    border-radius: 50%; background: var(--lavender); }
  .brand-name { position: absolute; left: 0; top: 230px; width: 800px; text-align: center;
    color: var(--white); font-size: 32px; font-weight: 400; }
  .brand-rule { position: absolute; left: 205px; top: 275px; width: 390px; height: 3px; background: var(--white); }

  .toolbar-icon { position: absolute; top: 300px; }
  .menu-icon { left: 22px; }
  .search-icon { left: 100px; }

  .book-now { position: absolute; left: 290px; top: 295px; width: 225px; height: 57px;
    border: 3px solid var(--lime); color: var(--lime); font-size: 30px;
    display: flex; align-items: center; justify-content: center; letter-spacing: 0.5px; }
  .phone-number { position: absolute; left: 566px; top: 304px; color: var(--white); font-size: 33px; }

  .panel { position: absolute; left: 0; width: 800px; overflow: hidden; }
  .panel-holistic { top: 370px; height: 275px;
    background: linear-gradient(100deg, #5f8a2a 0%, #a9c76a 30%, #e9ece3 55%, #9fbf57 80%, #4d7a1c 100%); }
  .panel-treatment { top: 657px; height: 293px;
    background: linear-gradient(180deg, #e6e9ee 0%, #c9d1dc 45%, #4a6fb0 70%, #2b3d66 100%); }
  .panel-about { top: 962px; height: 238px;
    background: linear-gradient(180deg, #b7737a 0%, #8b5a5e 40%, #3e2f38 75%, #1f1a22 100%); }

  .panel-badge { position: absolute; border-radius: 50%; display: flex; align-items: center;
    justify-content: center; text-align: center; color: var(--white); font-size: 20px; line-height: 1.35; }
  .badge-green { background: var(--lime-dark); border: 2px solid var(--lime); }
  .badge-violet { background: var(--violet-badge); }
  .badge-holistic { left: 511px; top: 17px; width: 190px; height: 176px; }
  .badge-treatment { left: 480px; top: 85px; width: 230px; height: 156px; }
  .badge-about { left: 480px; top: 73px; width: 234px; height: 172px; padding-bottom: 40px; }
</style>
</head>
<body>
  <header class="site-header">
    <div class="brand-mark"></div>
    <div class="brand-name">Evergrove Dental Carlton</div>
    <div class="brand-rule"></div>

    <svg class="toolbar-icon menu-icon" width="58" height="44" viewBox="0 0 58 44" aria-label="Menu">
      <rect x="2" y="4" width="54" height="5" fill="var(--lime)"/>
      <rect x="2" y="19" width="54" height="5" fill="var(--lime)"/>
      <rect x="2" y="34" width="54" height="5" fill="var(--lime)"/>
    </svg>
    <svg class="toolbar-icon search-icon" width="52" height="52" viewBox="0 0 52 52" aria-label="Search">
      <circle cx="20" cy="20" r="15" fill="none" stroke="var(--lime)" stroke-width="5"/>
      <line x1="31" y1="31" x2="48" y2="48" stroke="var(--lime)" stroke-width="7" stroke-linecap="round"/>
    </svg>

    <div class="book-now">BOOK NOW</div>
    <div class="phone-number">03/9000 4821</div>
  </header>

  <section class="panel panel-holistic" role="img" aria-label="Photo of a relaxed smiling woman outdoors among green leaves">
    <div class="panel-badge badge-green badge-holistic">HOLISTIC<br>APPROACH</div>
  </section>

  <section class="panel panel-treatment" role="img" aria-label="Photo of a bright dental treatment room with blue chairs">
    <div class="panel-badge badge-green badge-treatment">TREATMENT</div>
  </section>

  <section class="panel panel-about" role="img" aria-label="Photo of the practice street at dusk with a tram and practice sign">
    <div class="panel-badge badge-violet badge-about">ABOUT US</div>
  </section>
</body>
</html>
```